Salve Label

2.25 inch round label.

We are looking for a simple label, muted natural colors, sophisticated, elegant, calming.

Name of Product: Herbal Beeswax Salve
This scent is lavender - but there will be others scents
Want this label to be adaptable to other scents with simple color and word changes.

Other things to express on the label - all natural, calming, relaxing

Name of the Company: Tansy Ridge Farm
2 oz.

```html
<!DOCTYPE html>
<html lang="en">
<head>
<meta charset="utf-8">
<title>Herbal Beeswax Salve – Lavender Label</title>
<link rel="stylesheet" href="https://fonts.googleapis.com/css2?family=Roboto+Condensed:wght@300;400&family=Arimo:wght@400&display=swap">
<style>
  :root {
    --paper: #ffffff;
    --border-teal: #0c3a4f;
    --olive: #766a49;
    --olive-line: #7a6e4c;
  }
  html, body {
    margin: 0;
    padding: 0;
    width: 1200px;
    height: 1200px;
    overflow: hidden;
    background: var(--paper);
  }
  .canvas {
    position: relative;
    width: 1200px;
    height: 1200px;
    background: var(--paper);
  }
  .label-shape {
    position: absolute;
    inset: 0;
  }
  .label-text {
    position: absolute;
    left: 0;
    width: 1200px;
    margin: 0;
    text-align: center;
    color: var(--olive);
    white-space: nowrap;
  }
  .farm-name {
    top: 392px;
    font-family: "Roboto Condensed", sans-serif;
    font-weight: 400;
    font-size: 34px;
    letter-spacing: 1px;
  }
  .product-name {
    top: 440px;
    font-family: "Roboto Condensed", sans-serif;
    font-weight: 300;
    font-size: 122px;
    line-height: 98px;
    letter-spacing: -1px;
  }
  .scent {
    top: 770px;
    font-family: "Arimo", sans-serif;
    font-size: 46px;
    letter-spacing: 1px;
  }
  .net-weight {
    top: 818px;
    font-family: "Arimo", sans-serif;
    font-size: 26px;
    letter-spacing: 1px;
  }
</style>
</head>
<body>
<main class="canvas">
  <svg class="label-shape" width="1200" height="1200" viewBox="0 0 1200 1200">
    <circle class="botanical-border" cx="600" cy="600" r="375" fill="var(--border-teal)"
            role="img" aria-label="Band of white botanical silhouettes: leaves, sprigs and berry branches on deep teal"/>
    <circle class="gold-ring" cx="600" cy="600" r="311" fill="var(--paper)" stroke="var(--olive-line)" stroke-width="10"/>
    <circle class="inner-rule" cx="600" cy="600" r="299" fill="none" stroke="var(--olive-line)" stroke-width="1.5"/>
  </svg>

  <p class="label-text farm-name">Tansy Ridge Farm</p>
  <h1 class="label-text product-name">Herbal<br>Beeswax<br>SALVE</h1>
  <p class="label-text scent">Lavender</p>
  <p class="label-text net-weight">2 oz.</p>
</main>
</body>
</html>
```